Book Cover for a true crime story

Cover must be formatted for 6x9 size in pdf file. A tree branch running horizontally across the cover with a few green leaves and one shiny apple hanging from it. Background is bright light behind the apple. Apple has dagger entering near the top with the tip protruding on opposite side. Blood is running from the tip to form the book title below the apple: THE LAST COLD TRAIL. Header at top reads NOTES FROM YEARS SPENT WALKING THE DARKEST HALLWAYS. At bottom DET. WALTER BRISGANE, Ret
BVPS BURGLARY ASSAULT BUREAU.

(Back cover contains following text:)

BURGLARY ASSAULT BUREAU 1974: The commanding officer of the division, and the C/O of the Major Cases Unit, decide to break from the BVPS tradition of arbitrarily assigning partners. They take the unusual risk of allowing two detectives of equal supervisory rank (D-3) to decide if they want to work with one another. If the risk fails, the C/O’s would face department criticism for breaking with tradition and likely lose their assignments.

The Last Cold Trail is the true story of how Moss and Rudy teamed up to begin catching killers and solving murders in an unprecedented way - in a time without cell phones, computers, the internet or DNA - the 1970‘s. By all accounts, these were the glory years for BVPS.
(break here for the following endorsement)

Walter’s stories are based on real cases, the tough murder investigations. He solved the cases the way the public and his supervisors expected them to be solved: Hard work, doggedness, seeing details by bits and pieces and putting them together to complete the puzzle, outstanding interview and interrogation techniques, toughness, and the ability to be cold, hard, or compassionate when necessary. He and his partner solved more cases than all other teams combined. They were given the freedom to pursue their investigations as they saw fit because they had the confidence of their bosses, and they produced results.
Captain Harold Venkirk, Ret.
?Commanding Officer, BVPS Ridgeway Precinct (post Darnell Pruitt)
Past President, Bay Valley Officers Welfare Guild

• A book cover to capture attention.

```html
<!DOCTYPE html>
<html lang="en">
<head>
<meta charset="utf-8">
<title>The Last Cold Trail — Book Cover</title>
<link rel="stylesheet" href="https://fonts.googleapis.com/css2?family=PT+Sans:wght@400;700&display=swap">
<style>
  :root {
    --page-bg: #ffffff;
    --cover-edge: #3a3a3a;
    --cover-light: #ffffff;
    --cover-shade: #b5b5b5;
    --ink: #111111;
    --blood: #c8101a;
    --apple-red: #d8242a;
    --apple-deep: #a3151b;
    --leaf-green: #5c9a3c;
    --leaf-deep: #3f7a2a;
    --blade-dark: #2a2a2a;
  }
  html, body {
    margin: 0;
    padding: 0;
    width: 1200px;
    height: 1200px;
    overflow: hidden;
    background: var(--page-bg);
  }
  .canvas {
    position: relative;
    width: 1200px;
    height: 1200px;
  }
  .cover {
    position: absolute;
    left: 270px;
    top: 86px;
    width: 676px;
    height: 1014px;
    box-sizing: border-box;
    border: 2px solid var(--cover-edge);
    background: radial-gradient(ellipse 70% 55% at 52% 45%, var(--cover-light) 0%, #f3f3f3 45%, var(--cover-shade) 100%);
    overflow: hidden;
    font-family: "PT Sans", sans-serif;
    color: var(--ink);
  }
  .tagline {
    position: absolute;
    right: 46px;
    top: 36px;
    margin: 0;
    font-size: 27px;
    line-height: 31px;
    font-weight: 400;
    text-align: right;
  }
  .tagline span { display: block; }
  .artwork {
    position: absolute;
    left: 0;
    top: 112px;
    width: 676px;
    height: 400px;
  }
  .blood-drip {
    position: absolute;
    left: 100px;
    top: 500px;
    width: 28px;
    height: 362px;
  }
  .title {
    position: absolute;
    left: 0;
    top: 0;
    width: 100%;
    height: 100%;
    margin: 0;
    font-weight: 400;
    letter-spacing: -2px;
  }
  .title span {
    position: absolute;
    line-height: 1;
    white-space: nowrap;
  }
  .title .word-the   { left: 194px; top: 544px; font-size: 64px; }
  .title .word-last  { left: 136px; top: 593px; font-size: 130px; }
  .title .word-cold  { left: 140px; top: 687px; font-size: 130px; }
  .title .word-trail { left: 284px; top: 795px; font-size: 120px; }
  .author {
    position: absolute;
    left: 96px;
    top: 922px;
    margin: 0;
    font-size: 36px;
    line-height: 1;
    font-weight: 400;
  }
  .credential {
    position: absolute;
    left: 166px;
    top: 968px;
    margin: 0;
    font-size: 24px;
    line-height: 1;
    font-weight: 400;
  }
</style>
</head>
<body>
  <div class="canvas">
    <section class="cover">
      <p class="tagline">
        <span>Notes from years spent walking</span>
        <span>the darkest hallways</span>
      </p>

      <svg class="artwork" viewBox="0 0 676 400" role="img" aria-label="Illustration: a leafy tree branch across the cover with a shiny red apple hanging from it, pierced by a dagger whose tip drips blood">
        <defs>
          <linearGradient id="artTones" x1="0" y1="0" x2="1" y2="0">
            <stop offset="0%" stop-color="var(--leaf-deep)"/>
            <stop offset="28%" stop-color="var(--leaf-green)"/>
            <stop offset="50%" stop-color="var(--apple-red)"/>
            <stop offset="72%" stop-color="var(--apple-deep)"/>
            <stop offset="100%" stop-color="var(--blade-dark)"/>
          </linearGradient>
        </defs>
        <rect x="0" y="0" width="676" height="400" fill="url(#artTones)"/>
      </svg>

      <svg class="blood-drip" viewBox="0 0 28 362" role="img" aria-label="Illustration: a trail of blood running down from the dagger tip beside the title">
        <rect x="0" y="0" width="28" height="362" rx="14" fill="var(--blood)"/>
      </svg>

      <h1 class="title" aria-label="The Last Cold Trail">
        <span class="word-the">the</span>
        <span class="word-last">last</span>
        <span class="word-cold">cold</span>
        <span class="word-trail">trail</span>
      </h1>

      <p class="author">DET. Walter Brisgane</p>
      <p class="credential">RET BVPS Burglary Assault Bureau.</p>
    </section>
  </div>
</body>
</html>
```